Business Card Design Project

We require business cards to be produced with the following design
http://files.brieflanter.net/art_img/38217/49302/49302_5520914_38217_image.jpg
Rather than lantern yard, please use Dolvane as the comapny name.
Please also use the following contact details:
1.
Peter Halloway
Entrepreneur
07923418870
phalloway@dolvane.net
2.
Tom Brenner
Founder
07844512039
tbrenner@dolvane.net
Please add:
Facebook favicion mesharo.com/dolvane
Linked in favicon workvine/peterhalloway
Skype favicon phalloway
Linked in favicon linkedin/thomasbrenner
Skype favicon thomasbrenner
Google Plus favicon tombrenner@maildrop.net
To the back
Industry/Entity Type
Business
Look and feel
Each slider illustrates characteristics of the customer's brand and the style your logo design should communicate.

```html
<!DOCTYPE html>
<html lang="en">
<head>
<meta charset="utf-8">
<title>Dolvane — Business Card Back</title>
<link rel="stylesheet" href="https://fonts.googleapis.com/css2?family=PT+Sans:wght@400;700&display=swap">
<style>
  :root {
    --card-bg: #f1f2f0;
    --brand-red: #ff0000;
    --ink: #2b2b2b;
    --dot-social: #233f9c;
    --dot-network: #3a9fd3;
    --dot-chat: #54b8ea;
  }
  html, body {
    margin: 0;
    padding: 0;
    width: 1200px;
    height: 720px;
    overflow: hidden;
    background: var(--card-bg);
  }
  .card-back {
    position: relative;
    width: 1200px;
    height: 720px;
    background: var(--card-bg);
    font-family: "PT Sans", Arial, sans-serif;
  }
  .brand {
    position: absolute;
    left: 0;
    right: 0;
    top: 168px;
    display: flex;
    justify-content: center;
    align-items: center;
    gap: 22px;
  }
  .brand-dot {
    width: 46px;
    height: 46px;
    border-radius: 50%;
    background: var(--brand-red);
  }
  .brand-name {
    margin: 0;
    font-size: 96px;
    font-weight: 700;
    line-height: 1;
    color: var(--brand-red);
  }
  .contact-list {
    position: absolute;
    left: 371px;
    top: 388px;
    margin: 0;
    padding: 0;
    list-style: none;
  }
  .contact-item {
    display: flex;
    align-items: center;
    height: 60px;
    font-size: 42px;
    color: var(--ink);
    letter-spacing: -0.4px;
    white-space: nowrap;
  }
  .contact-icon {
    flex: none;
    width: 51px;
    height: 51px;
    border-radius: 50%;
    margin-right: 15px;
  }
  .contact-icon--social { background: var(--dot-social); }
  .contact-icon--network { background: var(--dot-network); }
  .contact-icon--chat { background: var(--dot-chat); width: 47px; height: 47px; margin-left: 2px; margin-right: 17px; }
</style>
</head>
<body>
  <main class="card-back">
    <div class="brand">
      <span class="brand-dot" aria-hidden="true"></span>
      <h1 class="brand-name">Dolvane</h1>
    </div>
    <ul class="contact-list">
      <li class="contact-item"><span class="contact-icon contact-icon--social" aria-hidden="true"></span>mesharo.com/dolvane</li>
      <li class="contact-item"><span class="contact-icon contact-icon--network" aria-hidden="true"></span>workvine/peterhalloway</li>
      <li class="contact-item"><span class="contact-icon contact-icon--chat" aria-hidden="true"></span>phalloway</li>
    </ul>
  </main>
</body>
</html>
```